Cryptocurrency Advisor Business Card

Dravelin Consulting Services is my company, which advises many projects in the ICO/Cryptocurrency industry. I'd like to get a sleek, preferably matte black or matte dark blue finish, business card with the company name (and simple logo w/ crypto feel) on one side and while the other side I'd like a small twitter and telegram logo together maybe separated by a / as it's the same, then an email and a phone logo so I can insert those specifics there (no address). Can have name then CEO section too. At the bottom of that section, find a place for more of a job description: ICO Advisor, World Champion Gamer, Esports Award Winner, Quorvane Expert. You can possibly design a simple logo or use something with a crypto twist or background, but nothing too complex. Rounded edges for printing not square.
Updates

Had personal issues taking a few days away from me being able to provide feedback and check designs, etc. Will be more active now finalizing design just needed few days from issue but all is sorted.

Target Market(s)

Cryptocurrency industry

Industry/Entity Type

Management Consulting

Contact Information for Business Card

Font styles to use
Sans Serif

Colors
5c5c5c
474747
757575
9d9d9d
aaaaaa
333333
0355a3

Requirements
Must have
• Refer to Details/Description
Nice to have
Should not have
• Address section

```html
<!DOCTYPE html>
<html lang="en">
<head>
<meta charset="utf-8">
<title>Dravelin Consulting – Business Card</title>
<link rel="stylesheet" href="https://fonts.googleapis.com/css2?family=Lato:wght@400;700&family=Oswald:wght@400;500&display=swap">
<style>
  :root {
    --stage: #1c1c1c;
    --card: #111111;
    --ink: #e6e6e6;
    --ink-soft: #aaaaaa;
    --rule: #333333;
    --accent: #9d9d9d;
  }
  * { box-sizing: border-box; margin: 0; padding: 0; }
  html, body { width: 1200px; height: 900px; overflow: hidden; }
  body {
    background: var(--stage);
    font-family: "Lato", sans-serif;
    color: var(--ink);
    position: relative;
  }
  .card {
    position: absolute;
    width: 560px;
    height: 320px;
    background: var(--card);
    border-radius: 22px;
    box-shadow: 0 18px 40px rgba(0,0,0,.55);
  }
  .card--brand { left: 120px; top: 90px; }
  .card--contact { left: 520px; top: 480px; }

  /* brand side */
  .brand {
    display: flex; align-items: center; gap: 12px;
    font-family: "Oswald", sans-serif;
    font-weight: 500;
    color: var(--ink);
    text-transform: uppercase;
    letter-spacing: .5px;
  }
  .brand__mark {
    width: 30px; height: 30px;
    border: 3px solid var(--ink);
    flex: none;
  }
  .card--brand .brand {
    position: absolute; left: 0; right: 0; top: 78px;
    justify-content: center; font-size: 30px;
  }
  .card--brand .rule {
    position: absolute; left: 150px; right: 150px; top: 160px;
    height: 1px; background: var(--rule);
  }
  .roles {
    position: absolute; left: 0; right: 0; top: 182px;
    text-align: center; font-size: 15px; line-height: 1.6;
    color: var(--ink);
  }
  .roles .dot {
    display: inline-block; width: 7px; height: 7px; border-radius: 50%;
    background: var(--ink); margin: 0 8px; vertical-align: middle;
  }

  /* contact side */
  .card--contact .brand {
    position: absolute; right: 40px; top: 48px; font-size: 24px;
  }
  .card--contact .rule--top {
    position: absolute; left: 300px; right: 36px; top: 110px;
    height: 1px; background: var(--rule);
  }
  .handle {
    position: absolute; right: 40px; top: 124px;
    font-size: 16px; color: var(--ink-soft);
  }
  .card--contact .rule--mid {
    position: absolute; left: 36px; right: 36px; top: 170px;
    height: 1px; background: var(--rule);
  }
  .person { position: absolute; left: 40px; top: 186px; }
  .person__name {
    font-family: "Oswald", sans-serif; font-weight: 500;
    font-size: 24px; text-transform: uppercase; letter-spacing: .5px;
  }
  .person__title { font-size: 16px; color: var(--ink-soft); margin-top: -2px; }
  .details { list-style: none; margin-top: 14px; font-size: 17px; }
  .details li { display: flex; align-items: center; gap: 9px; margin-bottom: 3px; }
  .details svg { width: 16px; height: 16px; fill: var(--ink-soft); flex: none; }
</style>
</head>
<body>

<section class="card card--brand" aria-label="Business card, brand side">
  <div class="brand"><span class="brand__mark"></span><span>Dravelin Consulting</span></div>
  <div class="rule"></div>
  <p class="roles">
    ICO Advisor<span class="dot"></span>World Champion Gamer<br>
    Esports Award Winner<span class="dot"></span>Quorvane Expert
  </p>
</section>

<section class="card card--contact" aria-label="Business card, contact side">
  <div class="brand"><span class="brand__mark"></span><span>Dravelin Consulting</span></div>
  <div class="rule rule--top"></div>
  <p class="handle">@dravelinconsulting</p>
  <div class="rule rule--mid"></div>
  <div class="person">
    <h1 class="person__name">Adrian Kessler</h1>
    <p class="person__title">CEO</p>
    <ul class="details">
      <li>
        <svg viewBox="0 0 24 24" aria-hidden="true"><path d="M6.6 10.8a15.1 15.1 0 0 0 6.6 6.6l2.2-2.2c.3-.3.7-.4 1-.2 1.1.4 2.3.6 3.6.6.6 0 1 .4 1 1V20c0 .6-.4 1-1 1C10.6 21 3 13.4 3 4c0-.6.4-1 1-1h3.5c.6 0 1 .4 1 1 0 1.3.2 2.5.6 3.6.1.3 0 .7-.2 1z"/></svg>
        <span>044-555 010 020</span>
      </li>
      <li>
        <svg viewBox="0 0 24 24" aria-hidden="true"><path d="M2 5h20v14H2zm2 2v.4l8 5.2 8-5.2V7zm0 2.8V17h16V9.8l-8 5.2z"/></svg>
        <span>info@dravelin.com</span>
      </li>
    </ul>
  </div>
</section>

</body>
</html>
```